Schönheitssalon benötigt Flyer
Sehr schöne Arbeit, perfekt den Kundengeschmack getroffen. Leider zusätzliche Kosten durch (nicht enthaltene) Stockphotos, aber der Flyer ist sehr schick.
Zielgruppe
Ein Schönheitssalon in einer Pafümerie bietet diverse Angebote im Paket an (Gesichtsreinigung, Massage, Peeling, Maniküre, Sugaring). Vorrangig sollen Frauen angesprochen werden.
Aufgabenstellung
Faltblatt, gefalzt auf DIN A6 , 4-seiter
Endformat: 21,0 cm x 14,85 cm
gefalztes Endformat: 10,5 cm x 14,85 cm
Wir wünschen uns eine freundliche und helle Gestaltung mit rosé, voilett, pastell.
Das Grau, was jetzt gerade hinter dem Logo ist, wirkt sehr altbacken und nicht zeitgemäß.

```html
<!DOCTYPE html>
<html lang="de">
<head>
<meta charset="utf-8">
<title>Rosenzeit – Faltblatt</title>
<link rel="stylesheet" href="https://fonts.googleapis.com/css2?family=Quicksand:wght@400;500;700&family=Great+Vibes&display=swap">
<style>
  :root {
    --page-bg: #efe3e5;
    --paper: #fbe9ec;
    --paper-light: #fff6f7;
    --rose: #e88fa3;
    --rose-strong: #e27890;
    --rose-soft: #f2c3cd;
    --text-grey: #8a7b7e;
    --band: #f1b9c4;
    --divider: #f3d3da;
    --white: #ffffff;
  }
  * { margin: 0; padding: 0; box-sizing: border-box; }
  html, body { width: 1200px; height: 3600px; overflow: hidden; }
  body {
    background: var(--page-bg);
    font-family: "Quicksand", sans-serif;
    position: relative;
  }
  .spread {
    position: absolute;
    left: 50px;
    width: 1100px;
    height: 778px;
    background: linear-gradient(135deg, var(--paper) 0%, var(--paper-light) 45%, var(--paper) 100%);
    box-shadow: 0 6px 22px rgba(160, 110, 120, 0.25);
    overflow: hidden;
  }
  .spread--outside { top: 982px; }
  .spread--inside { top: 1840px; }
  .fold { position: absolute; top: 0; left: 550px; width: 1px; height: 100%; background: var(--divider); opacity: 0.6; }
  .spread--inside .fold { height: 650px; }
  .abs { position: absolute; }

  /* outside – back panel */
  .intro {
    left: 60px; top: 100px; width: 430px;
    text-align: center; color: var(--rose);
    font-size: 17px; line-height: 1.55;
  }
  .intro p + p { margin-top: 26px; }
  .intro strong { font-weight: 700; color: var(--rose-strong); }
  .portrait {
    left: 205px; top: 400px; width: 180px; height: 180px; border-radius: 50%;
    background: radial-gradient(circle at 50% 40%, #f6ebe6 0%, #dfe3ea 60%, #c9d3df 100%);
    border: 5px solid var(--white);
  }
  .contact {
    left: 60px; top: 600px; width: 470px; text-align: center;
    color: var(--rose); font-size: 17px; line-height: 1.5;
  }
  .contact .hours { margin-top: 30px; }

  /* outside – front panel */
  .brand { left: 760px; top: 95px; width: 260px; text-align: center; }
  .brand__mark {
    width: 22px; height: 22px; border-radius: 50%;
    border: 2px solid var(--rose); margin: 0 auto 6px;
  }
  .brand__name { font-size: 42px; font-weight: 500; color: var(--rose); letter-spacing: 1px; }
  .tagline {
    left: 690px; top: 178px; width: 400px; text-align: center;
    font-family: "Great Vibes", cursive; font-size: 40px; color: var(--rose-soft);
  }
  .cover-photo { left: 0; top: 0; width: 1100px; height: 778px; }
  .cover-note {
    right: 48px; top: 690px; text-align: right;
    color: var(--white); font-size: 16px; line-height: 1.45;
  }

  /* inside */
  .band { left: 0; top: 0; width: 1100px; height: 778px; }
  .heading {
    color: var(--rose); font-size: 23px; font-weight: 500; letter-spacing: 3px;
    text-transform: uppercase;
  }
  .treatments { left: 50px; top: 50px; width: 480px; }
  .treatment { margin-top: 22px; color: var(--text-grey); }
  .treatment:first-of-type { margin-top: 26px; }
  .treatment__title {
    display: flex; justify-content: space-between;
    color: var(--rose); font-size: 17px;
  }
  .treatment__title span:last-child { white-space: nowrap; }
  .treatment__desc { font-size: 12.5px; line-height: 1.5; margin-top: 2px; width: 440px; }
  .extras { left: 573px; top: 50px; width: 480px; }
  .price-list { margin-top: 26px; list-style: none; font-size: 14px; color: var(--text-grey); }
  .price-list li { display: flex; height: 21px; align-items: center; }
  .price-list .item { flex: 1; }
  .price-list .price { width: 70px; text-align: right; color: var(--rose); }
  .sugaring { left: 573px; top: 400px; width: 480px; }
  .sugaring .price-list { margin-top: 18px; }
  .band-text {
    left: 50px; top: 726px; color: var(--white);
    font-size: 14px; font-weight: 700; letter-spacing: 2px; text-transform: uppercase;
  }
  .detail-photo { left: 640px; top: 640px; width: 360px; height: 138px; }
</style>
</head>
<body>

<section class="spread spread--outside" aria-label="Außenseite des Faltblatts">
  <div class="fold"></div>

  <div class="abs intro">
    <p>Erleben Sie eine Auszeit und schalten<br>Sie einfach mal ab bei einer<br>Wohlfühl-Gesichtsbehandlung.</p>
    <p><strong>Ich biete Ihnen auf Sie zugeschnittene<br>Kosmetikprogramme auf höchstem Niveau<br>mit hochwertigen Produkten.</strong></p>
    <p>Sie brauchen einfach nur genießen!<br>Ich freue mich auf Sie!</p>
  </div>

  <div class="abs portrait" role="img" aria-label="Porträtfoto der Kosmetikerin"></div>

  <div class="abs contact">
    <p>Musterstraße 120 a<br>12345 Musterstadt</p>
    <p class="hours">Öffnungszeiten<br>Do.: 9.30 – 19.00 Uhr<br>Fr.: 9.30 – 19.00 Uhr</p>
  </div>

  <div class="abs brand">
    <div class="brand__mark"></div>
    <div class="brand__name">Rosenzeit</div>
  </div>
  <div class="abs tagline">Entspannung &amp; Kosmetik</div>

  <svg class="abs cover-photo" viewBox="0 0 1100 778" role="img" aria-label="Foto einer entspannten Frau bei der Gesichtsbehandlung">
    <defs>
      <linearGradient id="coverTone" x1="0" y1="0" x2="1" y2="1">
        <stop offset="0" stop-color="#5a4540"/>
        <stop offset="0.35" stop-color="#e2b9a6"/>
        <stop offset="0.7" stop-color="#efd2c6"/>
        <stop offset="1" stop-color="#f6ece8"/>
      </linearGradient>
    </defs>
    <path d="M1100 255 L 830 255 A 300 300 0 0 0 543 778 L 1100 778 Z" fill="url(#coverTone)"/>
  </svg>
  <p class="abs cover-note">Im Haus der Stadt-<br>Parfümerie Halbach</p>
</section>

<section class="spread spread--inside" aria-label="Innenseite des Faltblatts">
  <div class="fold"></div>
  <svg class="abs band" viewBox="0 0 1100 778" aria-hidden="true">
    <path d="M0 700 C 300 650, 600 705, 1100 640 L 1100 778 L 0 778 Z" fill="var(--band)"/>
  </svg>

  <div class="abs treatments">
    <h2 class="heading">Gesichtsbehandlungen</h2>
    <div class="treatment">
      <div class="treatment__title"><span>Reinigungs-Behandlung:</span><span>ca. 60 Min. &nbsp; 35,- €</span></div>
      <p class="treatment__desc">Reinigung, Peeling, Ausreinigung, Maske &amp; Abschlusspflege</p>
    </div>
    <div class="treatment">
      <div class="treatment__title"><span>Basis-Behandlung:</span><span>ca. 90 Min. &nbsp; 49,- €</span></div>
      <p class="treatment__desc">Reinigung, Peeling, Ausreinigung, Augenbrauen-Korrektur,<br>Massage &amp; Maske, leichtes Make-Up auf Wunsch</p>
    </div>
    <div class="treatment">
      <div class="treatment__title"><span>Intensiv-Behandlung:</span><span>ca. 90 Min. &nbsp; 59,- €</span></div>
      <p class="treatment__desc">Reinigung, Peeling, Ausreinigung, Augenbrauen-Korrektur,<br>Ampulle, Massage, Maske &amp; Augenmaske, leichtes Make-Up<br>auf Wunsch</p>
    </div>
    <div class="treatment">
      <div class="treatment__title"><span>Verwöhn-Behandlung:</span><span>ca. 90 Min. &nbsp; 67,- €</span></div>
      <p class="treatment__desc">Reinigung, Peeling, Ausreinigung, Augenbrauen-Korrektur, Ampulle,<br>Massage, Maske, Hals- &amp; Dekolleté-Behandlung, leichtes Make-Up<br>auf Wunsch</p>
    </div>
    <div class="treatment">
      <div class="treatment__title"><span>Luxus-Behandlung:</span><span>ca. 120 Min. &nbsp; 81,- €</span></div>
      <p class="treatment__desc">Reinigung, Peeling, Ausreinigung, Augenbrauen-Korrektur,<br>Ampulle, Massage, Vlies-Maske, Augenmaske, Lippenpackung,<br>Handmassage &amp; Hals- &amp; Dekolleté-Behandlung,<br>leichtes Make-Up auf Wunsch</p>
    </div>
    <div class="treatment">
      <div class="treatment__title"><span>Teenie-Behandlung (bis 18 Jahre):</span><span>ca. 60 Min. &nbsp; 28,- €</span></div>
      <p class="treatment__desc">Reinigung, Peeling, Ausreinigung &amp; Maske</p>
    </div>
  </div>

  <div class="abs extras">
    <h2 class="heading">Zusatz- &amp; Einzelbehandlungen</h2>
    <ul class="price-list">
      <li><span class="item">Augenbrauen zupfen/wachsen</span><span class="price"></span><span class="price">8,- €</span></li>
      <li><span class="item">Augenbrauen färben</span><span class="price">6,50 €</span><span class="price">8,50 €</span></li>
      <li><span class="item">Wimpern färben</span><span class="price">7,- €</span><span class="price">9,- €</span></li>
      <li><span class="item">Augenbrauen &amp; Wimpern färben + zupfen</span><span class="price"></span><span class="price">21,- €</span></li>
      <li><span class="item">Wimpernwelle</span><span class="price">22,- €</span><span class="price">32,- €</span></li>
      <li><span class="item">Pflegende Maniküre (60 Min.)</span><span class="price">18,- €</span><span class="price">24,- €</span></li>
      <li><span class="item">Pflegende Maniküre + Lack</span><span class="price">24,- €</span><span class="price">32,- €</span></li>
      <li><span class="item">Wirkstoffampulle</span><span class="price"></span><span class="price">9,- €</span></li>
      <li><span class="item">Tages-Make-Up</span><span class="price"></span><span class="price">29,- €</span></li>
      <li><span class="item">Abend- / Foto-Make-Up</span><span class="price"></span><span class="price">35,- €</span></li>
      <li><span class="item">Braut-Make-Up (inkl. Probe)</span><span class="price"></span><span class="price">70,- €</span></li>
      <li><span class="item">Klassische Rückenmassage ca. 30 Min.</span><span class="price"></span><span class="price">25,- €</span></li>
    </ul>
  </div>

  <div class="abs sugaring">
    <h2 class="heading">Sugaring</h2>
    <ul class="price-list">
      <li><span class="item">Oberlippe</span><span class="price">9,- €</span><span class="price"></span></li>
      <li><span class="item">Oberlippe + Kinn</span><span class="price">14,- €</span><span class="price"></span></li>
      <li><span class="item">Arme</span><span class="price">ab 25,- €</span><span class="price"></span></li>
      <li><span class="item">Beine Unterschenkel</span><span class="price">25,- €</span><span class="price"></span></li>
      <li><span class="item">Beine komplett</span><span class="price">39,- €</span><span class="price"></span></li>
      <li><span class="item">Rücken</span><span class="price">ab 35,- €</span><span class="price"></span></li>
    </ul>
  </div>

  <svg class="abs detail-photo" viewBox="0 0 360 138" role="img" aria-label="Foto einer Gesichtsmassage mit Blüten">
    <defs>
      <linearGradient id="detailTone" x1="0" y1="0" x2="1" y2="0">
        <stop offset="0" stop-color="#f7e4e4" stop-opacity="0"/>
        <stop offset="0.25" stop-color="#f1cfc6"/>
        <stop offset="0.6" stop-color="#e9b5aa"/>
        <stop offset="1" stop-color="#f4d6d6" stop-opacity="0"/>
      </linearGradient>
    </defs>
    <rect x="0" y="0" width="360" height="138" fill="url(#detailTone)"/>
  </svg>

  <p class="abs band-text">Andere Bereiche auf Anfrage!</p>
</section>

</body>
</html>
```